CRPG is needing business cards, and stationary created.

Pixel Forge created a logo for our business, and now we are wanting business cards, and stationary. I have included two designs of the same logo. Please feel free to use them as you want. The name of the company is Cedar Ridge Property Group LLC, the address is 812 NE Willow Ln., Suite 9, the city & state is Bend, Oregon, zip code is 97815, Telephone number is 541-327-4489, Fax number is 541-327-6051, the name on the business card is Carl Whitby CMCA

Industry/Entity Type

Property Management

Contact Information for Business Card

The card needs to look professional. Upscale.

Requirements
Must have
• The colors we are using are on the logo that has been uploaded.

```html
<!DOCTYPE html>
<html lang="en">
<head>
<meta charset="utf-8">
<title>Cedar Ridge Property Group – Business Card</title>
<link rel="stylesheet" href="https://fonts.googleapis.com/css2?family=Poppins:wght@400;500;600&display=swap">
<style>
  :root {
    --backdrop: #e4e5e7;
    --navy: #1e2533;
    --navy-emboss: #2c3546;
    --navy-emboss-line: #3a4457;
    --green: #17805d;
    --ink: #3a3f47;
    --muted: #6b7079;
    --paper: #ffffff;
    --rule: #3a3f47;
  }
  * { box-sizing: border-box; margin: 0; padding: 0; }
  html, body { width: 1200px; height: 857px; overflow: hidden; }
  body {
    background: var(--backdrop);
    font-family: "Poppins", sans-serif;
    position: relative;
  }
  .card {
    position: absolute;
    top: 286px;
    width: 500px;
    height: 286px;
    box-shadow: 0 6px 18px rgba(0,0,0,0.12);
  }
  .card--front { left: 70px; background: var(--navy); }
  .card--back { left: 630px; background: var(--paper); }

  .brand {
    position: absolute;
    display: flex;
    align-items: center;
    gap: 12px;
  }
  .brand__mark { width: 34px; height: 34px; flex: none; }
  .brand__name {
    font-weight: 600;
    font-size: 22px;
    letter-spacing: 0.5px;
    line-height: 1.05;
    text-transform: uppercase;
  }
  .brand__tagline {
    display: block;
    font-weight: 600;
    font-size: 9px;
    letter-spacing: 3px;
    margin-top: 6px;
  }

  .card--front .brand { left: 100px; top: 112px; color: var(--navy-emboss); }
  .card--front .brand__mark { background: var(--navy-emboss); }
  .card--front .brand__name { text-shadow: 0 1px 0 var(--navy-emboss-line); }

  .card--back .brand { left: 40px; top: 106px; color: var(--green); }
  .card--back .brand__mark { background: var(--navy); }
  .card--back .brand__name { font-size: 19px; }
  .card--back .brand__tagline { color: var(--green); font-size: 8px; }

  .divider {
    position: absolute;
    left: 292px;
    top: 52px;
    width: 1px;
    height: 116px;
    background: var(--rule);
  }
  .contact {
    position: absolute;
    left: 310px;
    top: 50px;
    color: var(--ink);
  }
  .contact__name {
    font-weight: 600;
    font-size: 15px;
    color: var(--green);
    text-transform: uppercase;
    letter-spacing: 0.3px;
  }
  .contact__title { font-size: 10px; color: var(--muted); margin: 2px 0 6px; }
  .contact__list { list-style: none; }
  .contact__item {
    display: flex;
    align-items: center;
    gap: 7px;
    font-size: 11px;
    line-height: 18px;
  }
  .contact__icon { width: 13px; height: 13px; flex: none; }

  .address {
    position: absolute;
    left: 40px;
    bottom: 30px;
    font-size: 11px;
    color: var(--ink);
  }
  .address__company { color: var(--green); font-weight: 600; }
</style>
</head>
<body>

<section class="card card--front" aria-label="Card front">
  <div class="brand">
    <span class="brand__mark"></span>
    <span class="brand__name">Cedar Ridge
      <span class="brand__tagline">Rooted In Service</span>
    </span>
  </div>
</section>

<section class="card card--back" aria-label="Card back">
  <div class="brand">
    <span class="brand__mark"></span>
    <span class="brand__name">Cedar Ridge
      <span class="brand__tagline">Rooted In Service</span>
    </span>
  </div>

  <div class="divider"></div>

  <div class="contact">
    <p class="contact__name">Carl Whitby</p>
    <p class="contact__title">CMCA</p>
    <ul class="contact__list">
      <li class="contact__item">
        <svg class="contact__icon" viewBox="0 0 14 14" aria-hidden="true"><circle cx="7" cy="7" r="6.3" fill="none" stroke="#17805d" stroke-width="1.2"/><path d="M4.6 3.8l1.3 1.4-.7 1a4.5 4.5 0 0 0 2.6 2.6l1-.7 1.4 1.3-.8 1.1c-2.8-.3-5-2.5-5.3-5.3z" fill="#17805d"/></svg>
        541-327-4489
      </li>
      <li class="contact__item">
        <svg class="contact__icon" viewBox="0 0 14 14" aria-hidden="true"><circle cx="7" cy="7" r="6.3" fill="none" stroke="#17805d" stroke-width="1.2"/><rect x="4" y="5.5" width="6" height="3.5" fill="#17805d"/><rect x="5" y="3.5" width="4" height="2" fill="none" stroke="#17805d" stroke-width=".8"/></svg>
        541-327-6051
      </li>
      <li class="contact__item">
        <svg class="contact__icon" viewBox="0 0 14 14" aria-hidden="true"><circle cx="7" cy="7" r="6.3" fill="none" stroke="#17805d" stroke-width="1.2"/><rect x="3.8" y="4.8" width="6.4" height="4.4" fill="none" stroke="#17805d" stroke-width=".9"/><path d="M3.8 4.8l3.2 2.6 3.2-2.6" fill="none" stroke="#17805d" stroke-width=".9"/></svg>
        info@cedarridgepg.com
      </li>
      <li class="contact__item">
        <svg class="contact__icon" viewBox="0 0 14 14" aria-hidden="true"><circle cx="7" cy="7" r="6.3" fill="none" stroke="#17805d" stroke-width="1.2"/><circle cx="7" cy="7" r="3.3" fill="none" stroke="#17805d" stroke-width=".9"/><path d="M3.7 7h6.6M7 3.7c-1.5 2-1.5 4.6 0 6.6M7 3.7c1.5 2 1.5 4.6 0 6.6" fill="none" stroke="#17805d" stroke-width=".7"/></svg>
        www.cedarridgepg.com
      </li>
    </ul>
  </div>

  <p class="address"><span class="address__company">Cedar Ridge</span> – 812 NE Willow Ln., Suite 9 Bend, OR 97815</p>
</section>

</body>
</html>
```